Design a business card & stationary for a mortgage company

We are looking for a good looking business card design for our mortgage company that includes our logo. We received a free design as part of our logo project but we don't love it. The company is called "Pinecrest Mortgage Company" so we like waves and lighthouses. The logo should be included. We have a version in both vertical and horizontal that we have provided.

Industry/Entity Type

Finance

Contact Information for Business Card

This should include our new logo file

Requirements
Must have
• 3. The details you'd like on the card - name, title, phone, email, website, address, social media handles etc.
1. Marcus Hale
Vice President
732-419-6253
Fax 888-304-2918
mhale@pinecrestmortgage.example
NMLS 47162 - Company NMLS 61290
18 Larkin Ave
Toms River, NJ 08614

```html
<!DOCTYPE html>
<html lang="en">
<head>
<meta charset="utf-8">
<title>Pinecrest Mortgage Company – Business Card</title>
<link href="https://fonts.googleapis.com/css2?family=Josefin+Sans:wght@400;600&display=swap" rel="stylesheet">
<style>
  :root {
    --page: #ececec;
    --navy: #0f5287;
    --sky: #0a88c8;
    --name-blue: #2a9be0;
    --paper: #f4f4f4;
    --white: #ffffff;
  }
  * { box-sizing: border-box; margin: 0; padding: 0; }
  html, body { width: 1200px; height: 1200px; overflow: hidden; }
  body {
    background: var(--page);
    font-family: "Josefin Sans", sans-serif;
    position: relative;
  }
  .card {
    position: absolute;
    left: 227px;
    width: 746px;
    height: 425px;
    border-radius: 37px;
    overflow: hidden;
  }
  .card--front { top: 135px; background: var(--paper); }
  .card--back { top: 640px; background: var(--navy); }

  .wave { position: absolute; inset: 0; width: 100%; height: 100%; }

  .brand { position: absolute; text-align: right; font-weight: 400; line-height: 1; }
  .brand__name { display: block; font-size: 56px; letter-spacing: 1px; text-transform: uppercase; }
  .brand__sub { display: block; font-size: 20px; letter-spacing: 5px; text-transform: uppercase; margin-top: 8px; }
  .card--front .brand { right: 30px; top: 80px; color: var(--navy); }
  .card--back .brand { left: 0; right: 0; top: 150px; text-align: center; color: var(--white); }

  .person { position: absolute; left: 31px; top: 237px; color: var(--white); }
  .person__name { font-size: 25px; color: var(--name-blue); font-weight: 400; letter-spacing: 0.5px; }
  .person__title { font-size: 19px; margin-top: 6px; }
  .contacts { list-style: none; margin-top: 14px; }
  .contacts li { display: flex; align-items: center; font-size: 17px; height: 25.3px; }
  .contacts svg { width: 17px; height: 17px; margin-right: 11px; flex: none; }

  .licensing {
    position: absolute; right: 27px; top: 352px;
    text-align: right; color: var(--white); font-size: 19px; line-height: 25px;
  }
</style>
</head>
<body>

<section class="card card--front">
  <svg class="wave" viewBox="0 0 1200 684" preserveAspectRatio="none" aria-hidden="true">
    <path d="M20,318 C110,265 250,262 420,312 S820,470 1010,488 C1100,495 1160,440 1200,345 V684 H0 Z" fill="var(--sky)"/>
    <path d="M0,336 C100,285 250,290 420,340 S820,495 1010,502 C1100,505 1165,450 1200,360 V684 H0 Z" fill="var(--white)"/>
    <path d="M0,342 C100,292 250,296 420,346 S820,500 1010,507 C1100,510 1168,455 1200,368 V684 H0 Z" fill="var(--navy)"/>
  </svg>

  <div class="brand">
    <span class="brand__name">Pinecrest</span>
    <span class="brand__sub">Mortgage Company</span>
  </div>

  <div class="person">
    <p class="person__name">Marcus Hale</p>
    <p class="person__title">Vice President</p>
    <ul class="contacts">
      <li><svg viewBox="0 0 20 20"><circle cx="10" cy="10" r="10" fill="var(--sky)"/><path d="M6 7c1-2 7-2 8 0l-1 1.5h-6z M6.5 9h7l1 4h-9z" fill="var(--navy)"/></svg>732-419-6253</li>
      <li><svg viewBox="0 0 20 20"><circle cx="10" cy="10" r="10" fill="var(--sky)"/><rect x="6" y="5" width="8" height="10" rx="1" fill="var(--navy)"/></svg>888-304-2918</li>
      <li><svg viewBox="0 0 20 20"><circle cx="10" cy="10" r="10" fill="var(--sky)"/><rect x="5" y="6.5" width="10" height="7" fill="var(--navy)"/><path d="M5 6.5l5 4 5-4" stroke="var(--sky)" fill="none"/></svg>mhale@pinecrestmortgage.example</li>
      <li><svg viewBox="0 0 20 20"><circle cx="10" cy="10" r="10" fill="var(--sky)"/><circle cx="10" cy="10" r="5.5" fill="none" stroke="var(--navy)" stroke-width="1.6"/><path d="M4.5 10h11M10 4.5c-2.5 3-2.5 8 0 11M10 4.5c2.5 3 2.5 8 0 11" stroke="var(--navy)" fill="none"/></svg>www.pinecrestmortgage.example</li>
    </ul>
  </div>

  <div class="licensing">
    <p>NMLS 47162 - Company NMLS 61290</p>
    <p>18 Larkin Ave, Toms River, NJ 08614</p>
  </div>
</section>

<section class="card card--back">
  <div class="brand">
    <span class="brand__name">Pinecrest</span>
    <span class="brand__sub">Mortgage Company</span>
  </div>
</section>

</body>
</html>
```